Business Card Project for 'Manufacturing and Healthcare Business Improvement company.

I need a business card for a consulting company that does process improvement for manufacturing and healthcare companies. I had a contest for a logo, and I liked what we came up with for the logo.

I wasn't blown away by what I got for the business card. The designer tried and it was a decent design, but I was looking for a little more. I want something that looks professional, but is eye-catching enough that people say "that looks cool, where did you get it?"

I've uploaded some business card examples I found that I liked. Even though some of the examples have red and orange on them, I think I would stick with blues, grays and blacks since that matches the logo theme. As awesome as some of them look, I don't think that a single color card, like an all-black card, will work for me; but feel free to change my mind.

It might also be possible to incorporate elements from the logo into the card. I also like some of the elements that use circles or rectangles etc to separate the phone number, website etc.

I like it when people have used geometric shapes to break up the card into sections or to add borders to the card to complement the logo, not compete with it for attention. For example, the red and gray example that has a curve that separates the card into two parts. I've wondered, how it would look if the red area were blue and had an arrow separating the top and bottom, like the arrow on the logo. Maybe on the back there could be an element that mirrors the bar graph and arrow. Would those look interesting, or would they compete with the other elements too much?

I also uploaded some examples of cards I made up, either based on ideas I saw elsewhere or based on design elements that the logo had in his designs. If you wonder why the ones with "lorem ipsum" look like an amateur did them, it's because they did.

I also think that I may add a QR code at some point, so I would need a location for that, along with something that says what the QR links to, such as, "scan here to upload contact information" or something similar. I don't know if I want cards that require having special designs cut, but if you have the idea, go with it.

I don't want to limit anyone's creativity, so I'll leave it at that.

Target Market(s)

Healthcare and Manufacturing

Industry/Entity Type

Manufacturing

Contact Information for Business Card

Harborline Advisory Group LLC.
Owen Prescott MBA, LSSMBB
Managing Partner
o.prescott@harborlineadvisorygroupllc.com
(555) 987-2310

Font styles to use
Serif
Sans Serif

Colors

Designer to choose only greyscale colors for use in the design.

Requirements
Must have
• The logo.
Nice to have
• Even though some of the examples I uploaded have red and orange on them, I think I would stick with blues, grays and blacks since that matches the logo theme.

I also like some of the elements that use circles or rectangles etc to separate the phone number, website etc.

I like it when people have used geometric shapes to break up the card into sections or to add borders to the card to complement the logo, not compete with it for attention.

For example, the red and gray example that has a curve that separates the card into two parts. I've wondered, how it would look if the red area were blue and had an arrow separating the top and bottom, like the arrow on the logo. Maybe on the back there could be an element that mirrors the bar graph and arrow. Would those look interesting, or would they compete with the other elements too much?

It might also be possible to incorporate elements from the logo into the card.

I also think that I may add a QR code at some point, so I would need a location for that, along with something that says what the QR links to, such as, "scan here to upload contact information" or something similar.

It could have something somewhere saying "We use Lean, Six Sigma and TPM continuous improvement tools to improve manufacturing and healthcare businesses."
Should not have
• So many colors and elements that it is distracting. Should not be generic.

As awesome as some of them look, I don't think that a single color card, like an all-black card, will work for me; but feel free to change my mind.

I don't know if I want cards that require having special designs cut, but if you have the idea, go with it.

```html
<!DOCTYPE html>
<html lang="en">
<head>
<meta charset="utf-8">
<title>Harborline Advisory Group LLC – Business Card</title>
<link rel="stylesheet" href="https://fonts.googleapis.com/css2?family=Montserrat:wght@400;600;700;800&display=swap">
<style>
  :root {
    --page-bg: #e4e6e8;
    --card-dark: #33383e;
    --card-mid: #6c737a;
    --card-light: #b3b9bd;
    --back-dark: #7a8187;
    --back-light: #b6bcc0;
    --accent-blue: #4ea6dc;
    --text-white: #ffffff;
    --text-soft: #e9edf0;
  }
  * { margin: 0; padding: 0; box-sizing: border-box; }
  html, body {
    width: 1200px; height: 870px; overflow: hidden;
    background: var(--page-bg);
    font-family: "Montserrat", Arial, sans-serif;
  }
  .canvas { position: relative; width: 1200px; height: 870px; }

  .card {
    position: absolute; width: 700px; height: 400px; overflow: hidden;
    box-shadow: 0 6px 18px rgba(0, 0, 0, 0.18);
  }
  .card-front { left: 60px; top: 25px; }
  .card-back { left: 440px; top: 445px; }

  .card-art { position: absolute; inset: 0; }
  .card-front .card-art {
    background: linear-gradient(160deg, var(--card-dark) 0%, #4c5259 35%, var(--card-mid) 70%, var(--card-light) 100%);
  }
  .card-back .card-art {
    background: linear-gradient(160deg, var(--back-dark) 0%, #959ca1 45%, var(--back-light) 100%);
  }

  .company-mark {
    position: absolute; display: flex; align-items: center; gap: 12px;
  }
  .company-mark .mark-square {
    width: 26px; height: 26px; background: var(--accent-blue); flex: none;
  }
  .company-mark .mark-name {
    color: var(--text-white); font-weight: 700; font-size: 19px;
    line-height: 1.2; text-transform: uppercase; letter-spacing: 0.5px;
    white-space: nowrap;
  }
  .mark-line { display: block; }
  .card-front .company-mark { left: 60px; top: 66px; }
  .card-back .company-mark { right: 60px; bottom: 44px; }

  .person { position: absolute; left: 390px; top: 70px; width: 300px; text-align: center; }
  .person-name {
    color: var(--accent-blue); font-weight: 800; font-size: 26px;
    letter-spacing: 0.5px; text-transform: uppercase; white-space: nowrap;
  }
  .person-credentials { color: var(--text-soft); font-weight: 400; font-size: 17px; margin-top: 6px; }
  .person-title { color: var(--text-soft); font-weight: 600; font-size: 15px; margin-top: 4px; }

  .divider {
    position: absolute; left: 72px; top: 188px; width: 580px; height: 3px;
    background: var(--text-white);
  }

  .contact { position: absolute; left: 0; width: 100%; text-align: center; color: var(--text-white); }
  .contact-phone { top: 215px; }
  .contact-email { top: 285px; }
  .contact-icon { display: block; margin: 0 auto 4px; width: 24px; height: 24px; }
  .contact-text { font-weight: 700; font-size: 17px; white-space: nowrap; }
  .contact-email .contact-text { font-size: 16px; }
</style>
</head>
<body>
<main class="canvas">

  <section class="card card-front" aria-label="Business card front">
    <div class="card-art" role="img" aria-label="Grey background with a faint rising chart-line pattern"></div>

    <div class="company-mark">
      <span class="mark-square"></span>
      <span class="mark-name"><span class="mark-line">Harborline</span><span class="mark-line">Advisory Group LLC</span></span>
    </div>

    <div class="person">
      <p class="person-name">Owen Prescott</p>
      <p class="person-credentials">MBA, LSSMBB</p>
      <p class="person-title">Managing Partner</p>
    </div>

    <div class="divider"></div>

    <div class="contact contact-phone">
      <svg class="contact-icon" viewBox="0 0 24 24" aria-hidden="true">
        <circle cx="12" cy="12" r="10.5" fill="none" stroke="var(--text-white)" stroke-width="1.5"/>
        <path d="M8.5 6.8l1.8-.3 1 2.4-1.2 1c.6 1.3 1.6 2.3 2.9 2.9l1-1.2 2.4 1-.3 1.8c-.1.5-.6.8-1.1.8-4-.4-7-3.4-7.4-7.4 0-.5.4-1 .9-1z" fill="var(--text-white)"/>
      </svg>
      <p class="contact-text">(555) 987-2310</p>
    </div>

    <div class="contact contact-email">
      <svg class="contact-icon" viewBox="0 0 24 24" aria-hidden="true">
        <circle cx="12" cy="12" r="10.5" fill="none" stroke="var(--text-white)" stroke-width="1.5"/>
        <rect x="6.5" y="8" width="11" height="8" rx="1" fill="var(--text-white)"/>
        <path d="M6.8 8.5l5.2 4 5.2-4" fill="none" stroke="#6f767c" stroke-width="1.2"/>
      </svg>
      <p class="contact-text">o.prescott@harborlineadvisorygroupllc.com</p>
    </div>
  </section>

  <section class="card card-back" aria-label="Business card back">
    <div class="card-art" role="img" aria-label="Light grey background with a faint rising chart-line pattern"></div>

    <div class="company-mark">
      <span class="mark-square"></span>
      <span class="mark-name"><span class="mark-line">Harborline</span><span class="mark-line">Advisory Group LLC</span></span>
    </div>
  </section>

</main>
</body>
</html>
```